Kitchen manufaturer business card/logo design

I am a small kitchen manufacturing company that makes and installs all sorts of cabinetry.

The colours im looking to incorporate in the card are light/baby blue, white and black.

Incorporate 5 stars to show quality workmanship and product.

Looking for a modern classy design.
Updates

Hey guys, New idea. The logo should be made using HK in the most modern way possible as well as the full company name below it. Thanks.

Target Market(s)

Anyone with a home thats looking for a new cabinetry of any sort.

Industry/Entity Type

Business

Contact Information for Business Card

Harbor Kitchens
Ted Lowther
PH 0491 358 902
Email- harborkitchens@mailvane.example
ABN- 83 507 962 318
-Kitchens
-Vanities
-Laundries
-Media Units
-Studies
-Wardrobes
-3D Computer Designs

Requirements
Must have

• The front of the card must only have the company name.
The different types of cabinetry I do must be on the back of the card in point form but instead of using points use stars.
Nice to have
• Just think classy and quality

```html
<!DOCTYPE html>
<html lang="en">
<head>
<meta charset="utf-8">
<title>Harbor Kitchens – Business Card</title>
<link rel="stylesheet" href="https://fonts.googleapis.com/css2?family=Tinos:wght@400;700&family=Oswald:wght@500&family=Parisienne&display=swap">
<style>
  :root {
    --stage: #000000;
    --aqua: #3ff0f0;
    --aqua-floor: #5cf6f1;
    --aqua-pale: #a8fbf5;
    --ink: #0a0a0a;
    --white: #ffffff;
    --shadow: rgba(0, 0, 0, 0.35);
  }
  * { margin: 0; padding: 0; box-sizing: border-box; }
  html, body {
    width: 1067px;
    height: 1200px;
    overflow: hidden;
    background: var(--stage);
  }
  .sheet {
    position: relative;
    width: 1067px;
    height: 1200px;
  }
  .card {
    position: absolute;
    left: 67px;
    width: 933px;
    height: 533px;
    overflow: hidden;
  }
  /* Front */
  .card--front {
    top: 43px;
    background: var(--aqua);
  }
  .brand-mark {
    position: absolute;
    top: 170px;
    left: 0;
    width: 100%;
    text-align: center;
    font-family: "Tinos", serif;
    font-weight: 700;
    font-size: 120px;
    line-height: 1;
    color: var(--white);
  }
  .brand-name {
    position: absolute;
    top: 345px;
    left: 0;
    width: 100%;
    text-align: center;
    font-family: "Tinos", serif;
    font-weight: 700;
    font-size: 38px;
    letter-spacing: 0.36em;
    padding-left: 0.36em;
    color: var(--ink);
  }
  .quality-stars {
    position: absolute;
    top: 394px;
    left: 360px;
    width: 182px;
    height: 30px;
  }
  /* Back */
  .card--back {
    top: 621px;
    background: var(--aqua);
  }
  .back-planes {
    position: absolute;
    inset: 0;
  }
  .service-list {
    list-style: none;
    position: absolute;
    left: 58px;
    top: 40px;
    font-family: "Oswald", sans-serif;
    font-weight: 500;
    text-transform: uppercase;
    color: var(--ink);
    text-shadow: 3px 3px 2px var(--shadow);
    transform: skewY(4deg);
    transform-origin: left top;
  }
  .service-list li {
    font-size: 25px;
    line-height: 37px;
    letter-spacing: 0.01em;
  }
  .service-list li.service--large {
    font-size: 36px;
    line-height: 48px;
  }
  .service-list li:nth-child(5) { margin-top: 14px; }
  .holder-name {
    position: absolute;
    left: 560px;
    top: 40px;
    font-family: "Parisienne", cursive;
    font-size: 44px;
    color: var(--ink);
    text-shadow: 2px 2px 2px var(--shadow);
  }
  .contact-block {
    position: absolute;
    left: 340px;
    top: 190px;
    width: 580px;
    font-family: "Tinos", serif;
    color: var(--ink);
    text-shadow: 3px 3px 3px var(--shadow);
    transform: rotate(4deg);
    transform-origin: center;
    text-align: center;
  }
  .contact-block p { line-height: 1.2; }
  .contact-phone { font-size: 32px; }
  .contact-email { font-size: 27px; }
  .contact-abn { font-size: 32px; }
</style>
</head>
<body>
<main class="sheet">

  <section class="card card--front" aria-label="Card front">
    <div class="brand-mark">HK</div>
    <div class="brand-name">Harbor Kitchens</div>
    <svg class="quality-stars" viewBox="0 0 182 30" aria-label="Five stars">
      <defs>
        <polygon id="star" points="15,1 18.5,10.5 28.5,11 20.7,17.3 23.4,27 15,21.5 6.6,27 9.3,17.3 1.5,11 11.5,10.5" fill="#ffffff"/>
      </defs>
      <use href="#star" x="0"/>
      <use href="#star" x="38"/>
      <use href="#star" x="76"/>
      <use href="#star" x="114"/>
      <use href="#star" x="152"/>
    </svg>
  </section>

  <section class="card card--back" aria-label="Card back">
    <svg class="back-planes" viewBox="0 0 933 533" preserveAspectRatio="none" aria-hidden="true">
      <polygon points="0,453 333,315 600,533 0,533" fill="var(--aqua-floor)"/>
      <polygon points="333,0 933,0 933,533 600,533 333,315" fill="var(--aqua-pale)"/>
    </svg>

    <ul class="service-list">
      <li>-Kitchens</li>
      <li>-Vanities</li>
      <li>-Laundries</li>
      <li>-Media Units</li>
      <li class="service--large">-Studies</li>
      <li class="service--large">-Wardrobes</li>
      <li class="service--large">-3D Computer Designs</li>
    </ul>

    <div class="holder-name">Ted Lowther</div>

    <div class="contact-block">
      <p class="contact-phone">PH: 0491 358 902</p>
      <p class="contact-email">Email: harborkitchens@mailvane.example</p>
      <p class="contact-abn">ABN: 83 507 962 318</p>
    </div>
  </section>

</main>
</body>
</html>
```